Business Card Design for Pastor/Church Leadership - simple, elegant, "different"

Design a name card based on logo and color from our branding guide - see file "MBF Logo and Color".
The teal frame around the logo is not part of the logo and is a not necessary design element for the name card (as the attached PDF file may suggest).
The font suggested by branding is "Frutiger 55 Roman".
The file "not good.pdf", a sample of a name card that is NOT good.
- fonts too small to read
- the tagline on the logo "Still waters, open door" not easy to read with logo used in this design
- "MAPLE GROVE FELLOWSHIP" unnecessarily duplicated - possibly because logo too small
- not sure about the green frame, probably better to drop

Target Market(s)

broad, all people the pastor of an international church in Tokyo meets

Industry/Entity Type

Business

Contact Information for Business Card

Mattias R. Pellworth
Pastor
3-9-4 Kawaranodai, Shibuya-ku
Tokyo 150-0001 (Church)
2-21 Ochibamachi, Shibuya-ku
Tokyo 150-0035 (Home)
Tel: 03-5817-2963
E-mail: pastor@maplegrovefell.org
URL: http://www.maplegrovefell.org

Font styles to use
Sans Serif
Other font styles liked:
• Frutiger 55 Roman (want, not must)

Requirements
Must have
• must include logo
• must make use of the "bright turquoise color"
• Cyan = 59, Magenta = 0, Yellow=24, Black=0
• Red=3.1%, Green=91%, Blue=87.1%
• Key Info (name) must be easy to read (see notes on bad sample namecard attached)

```html
<!DOCTYPE html>
<html lang="en">
<head>
<meta charset="utf-8">
<title>Maple Grove Fellowship – Pastor Name Card</title>
<link rel="stylesheet" href="https://fonts.googleapis.com/css2?family=Source+Sans+3:ital,wght@0,400;0,600;0,700;1,400&display=swap">
<style>
  :root {
    --turquoise: #6bcbd0;
    --brand-teal: #5bc4c8;
    --slate: #576b6c;
    --paper: #ffffff;
    --backdrop: #ffffff;
  }
  * { box-sizing: border-box; margin: 0; padding: 0; }
  html, body {
    width: 1200px; height: 1000px; overflow: hidden;
    background: var(--backdrop);
    font-family: "Source Sans 3", sans-serif;
  }
  .name-card {
    position: absolute; left: 75px; top: 200px;
    width: 1050px; height: 598px;
    background: var(--paper);
    overflow: hidden;
  }
  .name-card__sweep { position: absolute; inset: 0; width: 100%; height: 100%; }
  .brand {
    position: absolute; left: 0; width: 595px; top: 0; height: 598px;
    text-align: center; color: var(--brand-teal);
  }
  .brand__mark {
    position: absolute; left: 267px; top: 180px;
    width: 60px; height: 60px; background: var(--brand-teal);
  }
  .brand__name {
    position: absolute; left: 0; right: 0; top: 420px;
    font-size: 34px; font-weight: 400; letter-spacing: 0.2px;
  }
  .brand__tagline {
    position: absolute; left: 0; right: 0; top: 492px;
    font-size: 29px; font-weight: 400;
  }
  .contact {
    position: absolute; right: 67px; top: 0; text-align: right;
  }
  .contact__name {
    position: absolute; right: 0; top: 48px; white-space: nowrap;
    font-size: 42px; font-weight: 700; color: var(--slate);
  }
  .contact__role {
    position: absolute; right: 0; top: 100px;
    font-size: 34px; font-style: italic; color: var(--paper);
  }
  .contact__lines {
    position: absolute; right: 0; top: 174px; white-space: nowrap;
    font-size: 22px; line-height: 31px; color: var(--paper);
  }
  .address {
    position: absolute; right: 0; white-space: nowrap;
    font-size: 22px; line-height: 40px; color: var(--slate);
  }
  .address--church { top: 350px; }
  .address--home { top: 457px; line-height: 37px; }
</style>
</head>
<body>
  <main class="name-card">
    <svg class="name-card__sweep" viewBox="0 0 1050 598" aria-hidden="true">
      <path d="M478,0 C525,280 585,500 665,545 C735,590 875,595 1050,598 L1050,0 Z" fill="var(--turquoise)"/>
    </svg>

    <section class="brand">
      <div class="brand__mark"></div>
      <h1 class="brand__name">MAPLE GROVE FELLOWSHIP</h1>
      <p class="brand__tagline">Still waters, open door</p>
    </section>

    <section class="contact" style="left:0;">
      <h2 class="contact__name">Mattias R. Pellworth</h2>
      <p class="contact__role">Pastor</p>
      <p class="contact__lines">
        03-5817-2963<br>
        pastor@maplegrovefell.org<br>
        www.maplegrovefell.org
      </p>
      <p class="address address--church">
        3-9-4 Kawaranodai, Shibuya-ku<br>
        Tokyo 150-0001 (Church)
      </p>
      <p class="address address--home">
        2-21 Ochibamachi, Shibuya-ku<br>
        Tokyo 150-0035 (Home)
      </p>
    </section>
  </main>
</body>
</html>
```